Design a New Site for a very cool Watch

We have the overall design element of the website and the banners in the PSD file. We need someone to finish our design in PSD and than convert to HTML. We have included the instructions, PSD file, images and all text.

We currently use Hubspot to host and make changes to our site. The entire design aspect is complete so all we need is some minor changes and additions within the photoshop design and than the coding into HTML.

Please only sign up if you understand photoshop and HTML conversion

Here is the DropBox link to the files
https://files.quorvel-share.net/s/pm4kx82lwq7dtne/Belthor%20Site.zip
Updates

We have the basic design concept in Photoshop.  We just need someone who can complete some changes, make some additions and convert to HTML

Target Market(s)

Watch Buyers

Requirements
Must have
• Must look like a professional luxury brand

Our brand colors are very basic with Black, White and Grey can be used

```html
<!DOCTYPE html>
<html lang="en">
<head>
<meta charset="utf-8">
<title>Belthor &amp; Co. — Time &amp; Space Fused Together</title>
<link href="https://fonts.googleapis.com/css2?family=Cinzel:wght@400;700&family=Arimo:wght@400;700&family=Tinos:wght@400;700&display=swap" rel="stylesheet">
<style>
  :root {
    --black: #000000;
    --ink: #111111;
    --white: #ffffff;
    --panel: #d3d3d3;
    --field: #5e5e5e;
    --field-text: #e6e6e6;
    --grey-btn: #555555;
    --muted: #6b6b6b;
    --caption: #666666;
  }
  * { margin: 0; padding: 0; box-sizing: border-box; }
  html, body { width: 706px; height: 1200px; overflow: hidden; background: var(--white); }
  body { position: relative; font-family: "Arimo", Arial, sans-serif; color: var(--ink); }
  a { color: inherit; text-decoration: none; }

  .site-header { position: absolute; left: 0; top: 0; width: 706px; height: 68px; }
  .brand { position: absolute; left: 16px; top: 8px; display: flex; align-items: center; gap: 14px; height: 52px; }
  .brand-square { width: 48px; height: 52px; border: 2px solid var(--black); }
  .brand-name { font-family: "Cinzel", serif; font-weight: 400; font-size: 33px; color: var(--black); letter-spacing: 0.5px; padding-left: 14px; border-left: 2px solid var(--black); line-height: 52px; }
  .utility-links { position: absolute; right: 16px; top: 50px; font-family: "Cinzel", serif; font-size: 10px; display: flex; gap: 9px; color: var(--black); }

  .main-nav { position: absolute; left: 0; top: 68px; width: 706px; height: 34px; background: var(--black); display: flex; justify-content: space-between; align-items: center; padding: 0 18px 0 20px; }
  .main-nav a { font-family: "Cinzel", serif; font-size: 11.5px; color: var(--white); letter-spacing: 0.6px; }

  .hero { position: absolute; left: 0; top: 102px; width: 706px; height: 366px; background: radial-gradient(ellipse 220px 140px at 420px 260px, #8b7773 0%, #3b3442 45%, #0a0b12 80%), var(--black); }
  .hero-title { position: absolute; left: 97px; top: 22px; width: 200px; height: 110px; color: var(--white); font-family: "Cinzel", serif; font-weight: 400; }
  .hero-title .line { display: block; font-size: 40px; line-height: 38px; }
  .hero-title .amp { position: absolute; left: 133px; top: 14px; font-size: 54px; line-height: 54px; }
  .hero-title .sub { display: block; font-size: 19px; line-height: 22px; margin-top: 18px; letter-spacing: 0.3px; white-space: nowrap; }
  .slider-dots { position: absolute; right: 10px; bottom: 8px; display: flex; gap: 3px; }
  .slider-dots span { width: 11px; height: 11px; border: 1.5px solid var(--white); border-radius: 50%; }
  .slider-dots .active { background: var(--white); }

  .about { position: absolute; left: 18px; top: 493px; width: 380px; }
  .section-title { font-family: "Cinzel", serif; font-weight: 400; font-size: 24px; color: var(--black); }
  .about p { margin-top: 14px; font-size: 8.7px; line-height: 10.5px; }
  .learn-more { display: block; margin-top: 6px; font-family: "Tinos", serif; font-weight: 700; font-size: 8.5px; }

  .featured { position: absolute; left: 18px; top: 614px; width: 390px; }
  .featured .section-title { font-size: 22px; }
  .featured .light { color: var(--muted); }
  .product { position: absolute; width: 180px; text-align: center; }
  .product-photo { width: 96px; height: 126px; margin: 0 auto; border-radius: 8px; }
  .product-name { margin-top: 10px; font-family: "Tinos", serif; font-weight: 400; font-size: 10.5px; color: var(--ink); }
  .product-edition { margin-top: 2px; font-family: "Tinos", serif; font-weight: 700; font-size: 8px; color: var(--caption); }

  .actions { position: absolute; left: 18px; top: 1044px; display: flex; gap: 27px; }
  .btn { height: 36px; display: flex; align-items: center; justify-content: center; font-family: "Cinzel", serif; font-size: 15px; color: var(--white); box-shadow: -6px 8px 6px -6px rgba(0,0,0,0.45); }
  .btn-dark { width: 182px; background: #222222; }
  .btn-grey { width: 130px; background: var(--grey-btn); }

  .register { position: absolute; left: 428px; top: 495px; width: 270px; height: 356px; background: var(--panel); border-radius: 4px; overflow: hidden; }
  .register-head { height: 45px; background: linear-gradient(#2e3033, #121315); color: var(--white); font-family: "Cinzel", serif; font-weight: 700; font-size: 15px; display: flex; align-items: center; justify-content: center; }
  .register-form { padding: 21px 0 0 38px; }
  .register-form .field { display: block; width: 194px; height: 23px; margin-bottom: 14px; background: var(--field); border-radius: 3px; color: var(--field-text); font-size: 8.5px; line-height: 23px; padding-left: 12px; }
  .register-btn { position: absolute; left: 146px; top: 301px; width: 88px; height: 29px; background: linear-gradient(#3a3a3a, #111); color: var(--white); font-family: "Cinzel", serif; font-weight: 700; font-size: 12px; display: flex; align-items: center; justify-content: center; border-radius: 2px; }

  .site-footer { position: absolute; left: 0; top: 1141px; width: 706px; height: 51px; background: var(--black); }
  .footer-nav { position: absolute; left: 13px; top: 19px; display: flex; gap: 4px; }
  .footer-nav a { font-family: "Cinzel", serif; font-size: 8.5px; color: var(--white); }
  .social { position: absolute; left: 413px; top: 16px; display: flex; gap: 4px; }
  .social span { width: 20px; height: 20px; border-radius: 50%; background: var(--white); }
  .footer-brand { position: absolute; right: 14px; top: 14px; display: flex; align-items: center; gap: 8px; }
  .footer-brand .brand-square { width: 18px; height: 20px; border: 1.5px solid var(--white); }
  .footer-brand .brand-name { font-size: 13px; line-height: 22px; color: var(--white); border-left: 1px solid var(--white); padding-left: 8px; letter-spacing: 0.3px; }
</style>
</head>
<body>
  <header class="site-header">
    <a class="brand" href="#"><span class="brand-square"></span><span class="brand-name">BELTHOR &amp; CO.™</span></a>
    <nav class="utility-links"><a href="#">AUTHENTICATION</a><a href="#">FAQ</a></nav>
  </header>

  <nav class="main-nav">
    <a href="#">Home</a><a href="#">About us</a><a href="#">Contact</a><a href="#">Collection</a><a href="#">Lifestyle</a><a href="#">Media</a><a href="#">Distributors</a><a href="#">Buy Now</a>
  </nav>

  <section class="hero" role="img" aria-label="Silver watch hands sweeping across a starry galaxy in deep space">
    <h1 class="hero-title"><span class="line">TIME</span><span class="line">SPACE</span><span class="amp">&amp;</span><span class="sub">FUSED TOGETHER</span></h1>
    <div class="slider-dots"><span></span><span></span><span class="active"></span><span></span><span></span></div>
  </section>

  <section class="about">
    <h2 class="section-title">ABOUT BELTHOR &amp; CO.</h2>
    <p>When the cofounders of Belthor &amp; Co. had their first meeting, a mantra was born: <b>Be Amazing!</b> They set out on a mission to create pieces that inspire and delight the senses and ones which, if held true to their mission, make an impact on the wearer.</p>
    <a class="learn-more" href="#">LEARN MORE</a>
  </section>

  <section class="featured">
    <h2 class="section-title"><span class="light">FEATURED</span> COLLECTION</h2>
  </section>

  <article class="product" style="left:-7px;top:660px;">
    <div class="product-photo" role="img" aria-label="Square watch with black dial, polished steel case and black strap" style="background:linear-gradient(#2a2a2a,#8d8f93 50%,#1a1a1a);"></div>
    <h3 class="product-name">Corvane Black Polished Case</h3>
    <p class="product-edition">Limited Edition 50 pieces</p>
  </article>
  <article class="product" style="left:199px;top:660px;">
    <div class="product-photo" role="img" aria-label="Square watch with white dial, steel case and white strap" style="background:linear-gradient(#d8d8d8,#9a9a9a 50%,#e4e4e4);"></div>
    <h3 class="product-name">Corvane White</h3>
    <p class="product-edition">Limited Edition 70 pieces</p>
  </article>
  <article class="product" style="left:-7px;top:850px;">
    <div class="product-photo" role="img" aria-label="Square watch with red dial, black case and red strap" style="background:linear-gradient(#d11a20,#2a1212 50%,#c0141a);"></div>
    <h3 class="product-name">Corvane Red / Black Diamonds</h3>
    <p class="product-edition">Limited Edition 35 pieces</p>
  </article>
  <article class="product" style="left:193px;top:850px;">
    <div class="product-photo" role="img" aria-label="Square watch with pink dial, steel case and pink strap" style="background:linear-gradient(#e96aa8,#a6a0a6 50%,#e24f98);"></div>
    <h3 class="product-name">Corvane Pink</h3>
    <p class="product-edition">Limited Edition 50 pieces</p>
  </article>

  <div class="actions">
    <a class="btn btn-dark" href="#">+&nbsp; MORE PRODUCTS</a>
    <a class="btn btn-grey" href="#">SHOP NOW</a>
  </div>

  <aside class="register">
    <h2 class="register-head">REGISTER YOUR WATCH</h2>
    <form class="register-form">
      <span class="field">First Name</span>
      <span class="field">Last Name</span>
      <span class="field">Email Address</span>
      <span class="field">Telephone</span>
      <span class="field">Certificate Card Number</span>
      <span class="field">Model Number</span>
    </form>
    <span class="register-btn">REGISTER</span>
  </aside>

  <footer class="site-footer">
    <nav class="footer-nav">
      <a href="#">Home</a><a href="#">About us</a><a href="#">Contact</a><a href="#">Collection</a><a href="#">Lifestyle</a><a href="#">Media</a><a href="#">Distributors</a><a href="#">Buy Now</a>
    </nav>
    <div class="social" aria-label="Social links"><span></span><span></span><span></span><span></span></div>
    <div class="footer-brand"><span class="brand-square"></span><span class="brand-name">BELTHOR &amp; CO.™</span></div>
  </footer>
</body>
</html>
```